Business Card Design and stationary (thank you cards)

I am basically starting a "handyman" business but have a little ego issue with that term. I have been a professional in the design and construction business for 30 years. I want simple…I will define the scope of work I do as i move forward, and it can vary and i want it to vary.

Target Market(s)

Homeowners mostly

Industry/Entity Type

Business

Contact Information for Business Card

Company Name is "Fix 9 the Nest" Dale R. Hobbins, 42 Bellamy Orchard Lane, Harwick Bay, Me, 04412 (but I may want to use a PO Box), Phone is 207-555-0172, email is dhobbins418@quillpost.example,

Font styles to use
Sans Serif

Requirements
Should not have
• anything pre designed….hammers or whatever…custom lines to make home features as shone but simple and elegant

```html
<!DOCTYPE html>
<html lang="en">
<head>
<meta charset="utf-8">
<title>Fix 9 the Nest — Business Cards</title>
<link rel="stylesheet" href="https://fonts.googleapis.com/css2?family=Ubuntu:ital,wght@0,400;0,500;0,700;1,500&display=swap">
<style>
  :root {
    --backdrop: #d6d6d4;
    --card: #f7f7f5;
    --band-blue: #2c5f8d;
    --brand-blue: #124c97;
    --accent-red: #bf1a0e;
    --text-blue: #2f5e8c;
    --white: #ffffff;
  }
  * { margin: 0; padding: 0; box-sizing: border-box; }
  html, body {
    width: 1200px; height: 1000px; overflow: hidden;
    background: var(--backdrop);
    font-family: "Ubuntu", sans-serif;
  }
  .stage { position: relative; width: 1200px; height: 1000px; }
  .card {
    position: absolute; left: 250px; width: 700px; height: 400px;
    background: var(--card);
    box-shadow: 0 6px 18px rgba(0,0,0,0.18);
    overflow: hidden;
  }
  .card--front { top: 70px; }
  .card--contact { top: 530px; }
  .card__bands { position: absolute; inset: 0; width: 700px; height: 400px; }
  .brand {
    position: absolute; left: 0; right: 0;
    display: flex; justify-content: center; align-items: center; gap: 16px;
  }
  .brand__mark { width: 22px; height: 22px; background: var(--brand-blue); }
  .brand__name {
    color: var(--brand-blue); font-weight: 700; letter-spacing: 1px;
    text-transform: uppercase;
  }
  .card--front .brand { top: 150px; }
  .card--front .brand__name { font-size: 58px; }
  .card--contact .brand { top: 36px; }
  .card--contact .brand__mark { width: 16px; height: 16px; }
  .card--contact .brand__name { font-size: 40px; }
  .contact__name {
    position: absolute; left: 0; right: 0; top: 108px; height: 84px;
    display: flex; align-items: center; justify-content: center;
    color: var(--white);
    font-size: 22px; font-weight: 500; font-style: italic;
  }
  .contact__lines {
    position: absolute; left: 34px; top: 214px;
    color: var(--text-blue); font-size: 18px; font-weight: 500; line-height: 30px;
  }
  .contact__address {
    position: absolute; right: 36px; top: 282px;
    color: var(--text-blue); font-size: 18px; font-weight: 500; line-height: 30px;
  }
</style>
</head>
<body>
<main class="stage">

  <section class="card card--front" aria-label="Business card front">
    <svg class="card__bands" viewBox="0 0 700 400" aria-hidden="true">
      <polygon points="0,0 320,0 336,14 0,14" fill="var(--band-blue)"/>
      <polygon points="328,0 700,0 700,14 344,14" fill="var(--accent-red)"/>
      <polygon points="0,364 440,364 462,400 0,400" fill="var(--band-blue)"/>
      <polygon points="450,386 700,386 700,400 458,400" fill="var(--accent-red)"/>
    </svg>
    <div class="brand">
      <span class="brand__mark"></span>
      <span class="brand__name">Fix 9 the Nest</span>
    </div>
  </section>

  <section class="card card--contact" aria-label="Business card contact side">
    <svg class="card__bands" viewBox="0 0 700 400" aria-hidden="true">
      <rect x="0" y="108" width="700" height="84" fill="var(--band-blue)"/>
      <rect x="0" y="206" width="8" height="46" fill="var(--accent-red)"/>
      <rect x="690" y="292" width="10" height="50" fill="var(--accent-red)"/>
      <polygon points="0,352 430,352 450,378 0,378" fill="var(--band-blue)"/>
      <polygon points="444,378 700,378 700,392 454,392" fill="var(--accent-red)"/>
    </svg>
    <div class="brand">
      <span class="brand__mark"></span>
      <span class="brand__name">Fix 9 the Nest</span>
    </div>
    <p class="contact__name">Dale R. Hobbins</p>
    <p class="contact__lines">Phone : 207-555-0172<br>Email : dhobbins418@quillpost.example</p>
    <p class="contact__address">42 Bellamy Orchard Lane<br>Harwick Bay, Me, 04412</p>
  </section>

</main>
</body>
</html>
```